Mortgage Protection Insurance Flyer

The target audience are new home owners so the design needs to be clean and simple.

This a primarily for Final Expense Insurance, but need an area where it says "We Also Specialize In:"
- Medicare Supplement Insurance (MediGap)
- Annuities
- Final Expense

All flyer versions need to be editable. Colors to be used are red, white or black. Refer to my website for colors and photos (brightmeadowcover.com). Will attach my logo and a flyer that I found online that is the format that I am looking for (for 8.5 in. x 11 in version). Need flyer in standard letter size 8.5 in. x11 in. but also in 8.5 in. x 5.5 in and 5.0 in. x 8.0 in. All sizes to be portrait oriented. If picked as winning design, need all flyer versions in full color, also in grey scale and files in all industry file types.

Content can be taken from my website..... brightmeadowcover.com

Do NOT submit if you are not willing to provide all versions as described above for the original project price.

Must use royalty-free stock photos please.

Target Market(s)

New homeowners looking for insurance to protect there mortgage payments

Industry/Entity Type

Life Insurance

Colors
f69fa3

Requirements
Must have
• Colors to be used are red, white or black.
• Need flyer in standard letter size 8.5 in. x11 in. but also in 3.5 in. x 8.5 in (Full Bleed 3.75 in by 8.75 in.) and 4.0 in. x 6.0 in. (Full Bleed 4.12 in x 6.12 in) Each design tailored to the size dimensions (So no squeezing 8.5 x 11 design into a 4.0 x 6.0 space.) All sizes to be portrait oriented. If picked as winning design, need all flyer versions in full color, also in grey scale and files in all file types.
• Do not need physical address on flyer, do need email address on flyer though - tkelvin@brightmeadowcover.com
• So phone number should be prominent, email address and website address should also be contact area.
• If you can not agree to terms above, do not submit any designs.
• Need facebook & twitter logos somewhere in contact info area.
Nice to have
• See sample flyers I have attached.
• White background with red used as primary graphic color and black used as secondary graphic if needed.
• font to be used should similar to one used in logo.

```html
<!DOCTYPE html>
<html lang="en">
<head>
<meta charset="utf-8">
<title>Mortgage Protection Insurance Flyer</title>
<link rel="stylesheet" href="https://fonts.googleapis.com/css2?family=Oswald:wght@700&family=Lato:wght@400;700;900&family=Rubik:wght@700&display=swap">
<style>
  :root{
    --accent:#e8141b;
    --accent-dark:#9c1a1d;
    --headline-accent:#f20d12;
    --ink:#1b1b1b;
    --text:#333;
    --paper:#fff;
    --side-colour:#f0b7b8;
    --side-grey:#dcdcdc;
  }
  *{box-sizing:border-box;margin:0;padding:0}
  html,body{width:1200px;height:1200px;overflow:hidden}
  body{font-family:"Lato",sans-serif;color:var(--text)}
  .board{position:relative;width:1200px;height:1200px;display:flex}
  .side{position:relative;height:1200px}
  .side-colour{width:617px;background:var(--side-colour)}
  .side-grey{width:583px;background:var(--side-grey);
    --accent:#6b6b6b;--accent-dark:#3d3d3d;--headline-accent:#5a5a5a}
  .card{position:absolute;width:525px;height:357px;background:var(--paper);overflow:hidden}
  .side-colour .front{left:58px;top:244px}
  .side-colour .back{left:58px;top:676px}
  .side-grey .front{left:18px;top:244px}
  .side-grey .back{left:18px;top:676px}
  .card-art{position:absolute;inset:0}
  .brand{position:absolute;font-family:"Lato",sans-serif;font-weight:900;color:var(--ink);
    font-size:9px;line-height:11px;letter-spacing:0;white-space:nowrap}
  .front .brand{left:35px;top:44px}
  .headline{position:absolute;left:33px;top:108px;font-family:"Oswald",sans-serif;font-weight:700;
    line-height:1;color:var(--ink);text-transform:uppercase}
  .headline .l1{display:block;font-size:31px}
  .headline .l2{display:block;font-size:27px;color:var(--headline-accent);margin-top:2px}
  .headline .l3{display:block;font-size:19px;margin-top:3px}
  .product-title{position:absolute;left:33px;top:235px;font-family:"Rubik",sans-serif;font-weight:700;
    font-size:15px;color:var(--headline-accent)}
  .product-body{position:absolute;left:34px;top:259px;width:260px;font-size:6.4px;line-height:8.4px;color:var(--text);text-align:justify}
  .product-body p+p{margin-top:6px}
  .benefits{position:absolute;left:339px;top:150px;width:163px;height:182px;border-radius:10px;
    background:linear-gradient(180deg,var(--accent),var(--accent-dark))}
  .benefits-tag{position:absolute;left:331px;top:164px;width:59px;height:11px;border-radius:0 6px 6px 0;
    background:#3a3a3a;color:#fff;font-size:6.5px;font-weight:700;padding:2px 0 0 8px}
  .benefit-list{position:absolute;left:348px;top:185px;width:146px;list-style:none;color:#fff;
    font-size:6.6px;line-height:8.4px;font-weight:700}
  .benefit-list li{position:relative;padding-left:11px;margin-bottom:8px}
  .tick{position:absolute;left:0;top:1px;width:7px;height:7px}
  .back-panel{position:absolute;left:0;top:0;width:296px;height:357px;background:var(--paper);
    box-shadow:3px 0 6px rgba(0,0,0,.25);z-index:1}
  .back .brand{left:38px;top:53px}
  .divider{position:absolute;left:166px;top:43px;width:1.5px;height:30px;background:var(--accent)}
  .address{position:absolute;left:180px;top:48px;font-size:8.5px;line-height:10.5px;color:var(--ink);white-space:nowrap}
  .about{position:absolute;left:28px;top:98px;width:236px;font-size:6.5px;line-height:8.4px;color:var(--ink)}
  .about p+p{margin-top:8px}
  .also-title{position:absolute;left:28px;top:177px;font-family:"Rubik",sans-serif;font-weight:700;font-size:10.5px;color:var(--headline-accent)}
  .also-list{position:absolute;left:28px;top:198px;width:230px;list-style:none;font-size:6.4px;line-height:8.2px;color:var(--ink)}
  .also-list li{position:absolute;padding-left:11px;white-space:nowrap}
  .also-list .tick{top:0}
  .also-list .medigap{left:0;top:0}
  .also-list .final{left:118px;top:0}
  .also-list .annuities{left:0;top:20px}
  .also-list .tick circle,.also-list .tick path{stroke:var(--accent)}
  .call{position:absolute;left:34px;top:290px;color:#fff}
  .call-label{font-size:11px;font-weight:700}
  .call-number{font-size:16.5px;font-weight:700;margin-top:2px;letter-spacing:.2px}
  .contact{position:absolute;left:152px;color:#fff;font-size:6.2px;font-weight:700;display:flex;align-items:center;gap:6px;white-space:nowrap}
  .contact.email{top:291px}
  .contact.web{top:311px}
  .contact svg{width:16px;height:16px}
  .social{position:absolute;left:262px;top:319px;display:flex;gap:2px}
  .social span{display:block;width:8px;height:8px;background:#fff;border-radius:1px}
</style>
</head>
<body>
<div class="board">

  <section class="side side-colour">
    <article class="card front">
      <svg class="card-art" viewBox="0 0 525 357" width="525" height="357">
        <defs>
          <linearGradient id="photoC" x1="0" y1="0" x2="1" y2="0">
            <stop offset="0" stop-color="#fff"/>
            <stop offset=".45" stop-color="#d8c4a4"/>
            <stop offset=".75" stop-color="#9a7b68"/>
            <stop offset="1" stop-color="#cfc6b8"/>
          </linearGradient>
        </defs>
        <g role="img" aria-label="Photo of a young family sitting on the front steps of their new home">
          <path d="M232,0 H525 V235 C470,200 400,186 300,188 C200,191 100,205 0,200 V85 C110,92 205,62 232,0 Z" fill="url(#photoC)"/>
        </g>
        <path d="M0,82 C110,92 205,60 228,0" fill="none" stroke="#1b1b1b" stroke-width="3"/>
        <path d="M0,88 C118,98 212,64 238,0" fill="none" stroke="#e8141b" stroke-width="2"/>
        <path d="M0,198 C100,206 210,190 345,180" fill="none" stroke="#1b1b1b" stroke-width="5"/>
        <path d="M0,210 C120,222 225,198 345,188" fill="none" stroke="#e8141b" stroke-width="2"/>
        <path d="M498,205 C508,212 518,222 525,226" fill="none" stroke="#1b1b1b" stroke-width="4"/>
        <path d="M498,218 C508,226 518,236 525,240" fill="none" stroke="#e8141b" stroke-width="3"/>
        <rect x="0" y="338" width="525" height="2" fill="#1b1b1b"/>
        <rect x="0" y="343" width="525" height="14" fill="#f20d12"/>
      </svg>
      <div class="brand">BRIGHT MEADOW COVER</div>
      <h1 class="headline"><span class="l1">Our</span><span class="l2">Plans Are</span><span class="l3">Based On Yours</span></h1>
      <h2 class="product-title">Mortgage Protection Insurance</h2>
      <div class="product-body">
        <p>Mortgage Protection Insurance (MPI) is a type of decreasing term life insurance policy designed to pay off your mortgage if you were to pass away — and many policies also cover mortgage payments (usually for a limited period of time) if you become disabled.</p>
        <p>Unforeseen events and a lack of the right kind of insurance can spell trouble quickly. Contact us today, to set up a free assessment time. We will analyze your insurance needs and get you and your family the right coverage quickly at a budget friendly price.</p>
      </div>
      <div class="benefits"></div>
      <div class="benefits-tag">Benefits:</div>
      <ul class="benefit-list">
        <li><svg class="tick" viewBox="0 0 10 10"><circle cx="5" cy="5" r="4.2" fill="none" stroke="#fff" stroke-width="1"/><path d="M3,5.2 L4.5,6.6 L7,3.8" fill="none" stroke="#fff" stroke-width="1"/></svg>Guaranteed approval. Even if you’re in poor health or work in a dangerous profession, there is guaranteed approval with no medical exams or lab tests.</li>
        <li><svg class="tick" viewBox="0 0 10 10"><circle cx="5" cy="5" r="4.2" fill="none" stroke="#fff" stroke-width="1"/><path d="M3,5.2 L4.5,6.6 L7,3.8" fill="none" stroke="#fff" stroke-width="1"/></svg>No guesswork. The check goes straight to the lender for the exact mortgage balance, so there’ll always be enough and your family won’t have to handle the money.</li>
        <li><svg class="tick" viewBox="0 0 10 10"><circle cx="5" cy="5" r="4.2" fill="none" stroke="#fff" stroke-width="1"/><path d="M3,5.2 L4.5,6.6 L7,3.8" fill="none" stroke="#fff" stroke-width="1"/></svg>Disability protection. Many MPI policies make mortgage payments (usually for a limited time) if you become disabled or lose your job.</li>
      </ul>
    </article>

    <article class="card back">
      <div class="back-panel">
        <svg class="card-art" viewBox="0 0 296 357" width="296" height="357">
          <defs>
            <linearGradient id="footC" x1="0" y1="0" x2="0" y2="1">
              <stop offset="0" stop-color="#e8141b"/>
              <stop offset="1" stop-color="#8e1a1c"/>
            </linearGradient>
          </defs>
          <path d="M0,252 C70,236 160,262 296,258" fill="none" stroke="#1b1b1b" stroke-width="5"/>
          <path d="M0,264 C80,248 165,274 296,268 V357 H0 Z" fill="url(#footC)"/>
        </svg>
        <div class="brand">BRIGHT MEADOW COVER</div>
        <div class="divider"></div>
        <div class="address">PO Box 214<br>Pine Hollow, ID 83801</div>
        <div class="about">
          <p>We have been helping clients in Northern Idaho/Eastern Washington prepare for the unknown.</p>
          <p>We have access to the industry’s top insurance carriers so you can get the right coverage, that fits your budget.</p>
          <p>Find out how we can give you the peace of mind of knowing your family will not have a financial burden if something were to happen to you.</p>
        </div>
        <h3 class="also-title">We Also Specialize In:</h3>
        <ul class="also-list">
          <li class="medigap"><svg class="tick" viewBox="0 0 10 10"><circle cx="5" cy="5" r="4.2" fill="none" stroke-width="1"/><path d="M3,5.2 L4.5,6.6 L7,3.8" fill="none" stroke-width="1"/></svg>Medicare Supplement<br>Insurance (Medigap)</li>
          <li class="final"><svg class="tick" viewBox="0 0 10 10"><circle cx="5" cy="5" r="4.2" fill="none" stroke-width="1"/><path d="M3,5.2 L4.5,6.6 L7,3.8" fill="none" stroke-width="1"/></svg>Final Expense Insurance</li>
          <li class="annuities"><svg class="tick" viewBox="0 0 10 10"><circle cx="5" cy="5" r="4.2" fill="none" stroke-width="1"/><path d="M3,5.2 L4.5,6.6 L7,3.8" fill="none" stroke-width="1"/></svg>Annuities</li>
        </ul>
        <div class="call"><div class="call-label">Call us now:</div><div class="call-number">(208)555.0147</div></div>
        <div class="contact email"><svg viewBox="0 0 16 16"><circle cx="8" cy="8" r="7" fill="none" stroke="#fff" stroke-width="1"/><rect x="4.5" y="5.5" width="7" height="5" fill="none" stroke="#fff" stroke-width=".9"/><path d="M4.5,5.5 L8,8.3 L11.5,5.5" fill="none" stroke="#fff" stroke-width=".9"/></svg>tkelvin@brightmeadowcover.com</div>
        <div class="contact web"><svg viewBox="0 0 16 16"><circle cx="8" cy="8" r="7" fill="none" stroke="#fff" stroke-width="1"/><circle cx="8" cy="8" r="4" fill="none" stroke="#fff" stroke-width=".9"/><path d="M4,8 H12 M8,4 C6,6 6,10 8,12 C10,10 10,6 8,4" fill="none" stroke="#fff" stroke-width=".8"/></svg>brightmeadowcover.com</div>
        <div class="social"><span></span><span></span></div>
      </div>
    </article>
  </section>

  <section class="side side-grey">
    <article class="card front">
      <svg class="card-art" viewBox="0 0 525 357" width="525" height="357">
        <defs>
          <linearGradient id="photoG" x1="0" y1="0" x2="1" y2="0">
            <stop offset="0" stop-color="#fff"/>
            <stop offset=".45" stop-color="#c4c4c4"/>
            <stop offset=".75" stop-color="#6e6e6e"/>
            <stop offset="1" stop-color="#c8c8c8"/>
          </linearGradient>
        </defs>
        <g role="img" aria-label="Greyscale photo of a young family sitting on the front steps of their new home">
          <path d="M232,0 H525 V235 C470,200 400,186 300,188 C200,191 100,205 0,200 V85 C110,92 205,62 232,0 Z" fill="url(#photoG)"/>
        </g>
        <path d="M0,82 C110,92 205,60 228,0" fill="none" stroke="#1b1b1b" stroke-width="3"/>
        <path d="M0,88 C118,98 212,64 238,0" fill="none" stroke="#6b6b6b" stroke-width="2"/>
        <path d="M0,198 C100,206 210,190 345,180" fill="none" stroke="#1b1b1b" stroke-width="5"/>
        <path d="M0,210 C120,222 225,198 345,188" fill="none" stroke="#6b6b6b" stroke-width="2"/>
        <path d="M498,205 C508,212 518,222 525,226" fill="none" stroke="#1b1b1b" stroke-width="4"/>
        <path d="M498,218 C508,226 518,236 525,240" fill="none" stroke="#6b6b6b" stroke-width="3"/>
        <rect x="0" y="338" width="525" height="2" fill="#1b1b1b"/>
        <rect x="0" y="343" width="525" height="14" fill="#6b6b6b"/>
      </svg>
      <div class="brand">BRIGHT MEADOW COVER</div>
      <h1 class="headline"><span class="l1">Our</span><span class="l2">Plans Are</span><span class="l3">Based On Yours</span></h1>
      <h2 class="product-title">Mortgage Protection Insurance</h2>
      <div class="product-body">
        <p>Mortgage Protection Insurance (MPI) is a type of decreasing term life insurance policy designed to pay off your mortgage if you were to pass away — and many policies also cover mortgage payments (usually for a limited period of time) if you become disabled.</p>
        <p>Unforeseen events and a lack of the right kind of insurance can spell trouble quickly. Contact us today, to set up a free assessment time. We will analyze your insurance needs and get you and your family the right coverage quickly at a budget friendly price.</p>
      </div>
      <div class="benefits"></div>
      <div class="benefits-tag">Benefits:</div>
      <ul class="benefit-list">
        <li><svg class="tick" viewBox="0 0 10 10"><circle cx="5" cy="5" r="4.2" fill="none" stroke="#fff" stroke-width="1"/><path d="M3,5.2 L4.5,6.6 L7,3.8" fill="none" stroke="#fff" stroke-width="1"/></svg>Guaranteed approval. Even if you’re in poor health or work in a dangerous profession, there is guaranteed approval with no medical exams or lab tests.</li>
        <li><svg class="tick" viewBox="0 0 10 10"><circle cx="5" cy="5" r="4.2" fill="none" stroke="#fff" stroke-width="1"/><path d="M3,5.2 L4.5,6.6 L7,3.8" fill="none" stroke="#fff" stroke-width="1"/></svg>No guesswork. The check goes straight to the lender for the exact mortgage balance, so there’ll always be enough and your family won’t have to handle the money.</li>
        <li><svg class="tick" viewBox="0 0 10 10"><circle cx="5" cy="5" r="4.2" fill="none" stroke="#fff" stroke-width="1"/><path d="M3,5.2 L4.5,6.6 L7,3.8" fill="none" stroke="#fff" stroke-width="1"/></svg>Disability protection. Many MPI policies make mortgage payments (usually for a limited time) if you become disabled or lose your job.</li>
      </ul>
    </article>

    <article class="card back">
      <div class="back-panel">
        <svg class="card-art" viewBox="0 0 296 357" width="296" height="357">
          <defs>
            <linearGradient id="footG" x1="0" y1="0" x2="0" y2="1">
              <stop offset="0" stop-color="#6b6b6b"/>
              <stop offset="1" stop-color="#3a3a3a"/>
            </linearGradient>
          </defs>
          <path d="M0,252 C70,236 160,262 296,258" fill="none" stroke="#1b1b1b" stroke-width="5"/>
          <path d="M0,264 C80,248 165,274 296,268 V357 H0 Z" fill="url(#footG)"/>
        </svg>
        <div class="brand">BRIGHT MEADOW COVER</div>
        <div class="divider"></div>
        <div class="address">PO Box 214<br>Pine Hollow, ID 83801</div>
        <div class="about">
          <p>We have been helping clients in Northern Idaho/Eastern Washington prepare for the unknown.</p>
          <p>We have access to the industry’s top insurance carriers so you can get the right coverage, that fits your budget.</p>
          <p>Find out how we can give you the peace of mind of knowing your family will not have a financial burden if something were to happen to you.</p>
        </div>
        <h3 class="also-title">We Also Specialize In:</h3>
        <ul class="also-list">
          <li class="medigap"><svg class="tick" viewBox="0 0 10 10"><circle cx="5" cy="5" r="4.2" fill="none" stroke-width="1"/><path d="M3,5.2 L4.5,6.6 L7,3.8" fill="none" stroke-width="1"/></svg>Medicare Supplement<br>Insurance (Medigap)</li>
          <li class="final"><svg class="tick" viewBox="0 0 10 10"><circle cx="5" cy="5" r="4.2" fill="none" stroke-width="1"/><path d="M3,5.2 L4.5,6.6 L7,3.8" fill="none" stroke-width="1"/></svg>Final Expense Insurance</li>
          <li class="annuities"><svg class="tick" viewBox="0 0 10 10"><circle cx="5" cy="5" r="4.2" fill="none" stroke-width="1"/><path d="M3,5.2 L4.5,6.6 L7,3.8" fill="none" stroke-width="1"/></svg>Annuities</li>
        </ul>
        <div class="call"><div class="call-label">Call us now:</div><div class="call-number">(208)555.0147</div></div>
        <div class="contact email"><svg viewBox="0 0 16 16"><circle cx="8" cy="8" r="7" fill="none" stroke="#fff" stroke-width="1"/><rect x="4.5" y="5.5" width="7" height="5" fill="none" stroke="#fff" stroke-width=".9"/><path d="M4.5,5.5 L8,8.3 L11.5,5.5" fill="none" stroke="#fff" stroke-width=".9"/></svg>tkelvin@brightmeadowcover.com</div>
        <div class="contact web"><svg viewBox="0 0 16 16"><circle cx="8" cy="8" r="7" fill="none" stroke="#fff" stroke-width="1"/><circle cx="8" cy="8" r="4" fill="none" stroke="#fff" stroke-width=".9"/><path d="M4,8 H12 M8,4 C6,6 6,10 8,12 C10,10 10,6 8,4" fill="none" stroke="#fff" stroke-width=".8"/></svg>brightmeadowcover.com</div>
        <div class="social"><span></span><span></span></div>
      </div>
    </article>
  </section>

</div>
</body>
</html>
```